SEAFOOD PACKAGING (Products for consumer)

We are looking to create packaging for various seafood products such as octopus and squid. We plan to sell our products in upscale supermarkets.

We are specializing in cut octopus this time.

Please include our company logo. Also, please leave a transparent area so that customers can see the product inside.
Updates

We want to show what is inside, so a picture of the octopus is not required. We need something simple and sophisticated.

Target Market(s)

upscale store in US and ASIA

Industry/Entity Type

Fisheries dealer

Requirements
Must have
• Please include the attached logo,Blue one is preferred.Please leave a transparent part so that the contents of the product can be seen by the consumer.1. product name on packaging →CUT OCTOPUS,TAKO SASHIMI,Highest quality,Top quality etc... 3. What text information should be on the packaging →(It may be edited, but this is the image) The raw materials are caught in a very clean environment and processed in a modern factory with ZEK certification. We are committed to additive-free products. 4. Packing size(cm/inch)→it will be about 19cm*22cm. 5. what kind of packaging do you use →PP or PA 6. dll →ai,jag
Nice to have
• https://quillmora.example/shots/4829174-Velka-Reef We need something simple and sophisticated like this one.
Should not have
• We want to show what is inside, so a picture of the octopus is not required. We need something simple and sophisticated.

```html
<!DOCTYPE html>
<html lang="en">
<head>
<meta charset="utf-8">
<title>MARLO Cut Octopus – Tako Sashimi</title>
<link href="https://fonts.googleapis.com/css2?family=Arvo:wght@700&family=Montserrat:wght@700&family=Noto+Serif:wght@400&family=Merriweather:wght@300&family=Oswald:wght@300;400;600&family=Fira+Sans+Condensed:wght@500&display=swap" rel="stylesheet">
<style>
  :root {
    --cream: #f6efe5;
    --navy: #2f5186;
    --mid-blue: #5b84c4;
    --sky: #7aaade;
    --deep-wave: #5e7fbe;
    --red: #c8262b;
    --bronze: #a86d2a;
    --rule: #c0843d;
    --white: #ffffff;
  }
  * { margin: 0; padding: 0; box-sizing: border-box; }
  html, body { width: 1037px; height: 1200px; overflow: hidden; background: var(--cream); }
  .package {
    position: relative;
    width: 1037px;
    height: 1200px;
    background: var(--cream);
    overflow: hidden;
  }
  .waves { position: absolute; inset: 0; width: 100%; height: 100%; }

  .brand-tab { position: absolute; left: 81px; top: 0; width: 161px; height: 192px; }
  .brand-name {
    position: absolute; left: 81px; top: 108px; width: 161px;
    text-align: center;
    font-family: "Montserrat", sans-serif; font-weight: 700; font-size: 32px;
    letter-spacing: 2px; color: var(--navy);
  }

  .tagline-top {
    position: absolute; left: 0; width: 100%; text-align: center;
    top: 106px;
    font-family: "Oswald", sans-serif; font-weight: 600; font-size: 27px;
    letter-spacing: 6px; color: var(--red);
  }
  .tagline-natural {
    position: absolute; left: 0; width: 100%; text-align: center;
    top: 143px;
    font-family: "Fira Sans Condensed", sans-serif; font-weight: 500; font-size: 27px;
    letter-spacing: 5px; color: var(--bronze);
  }

  .seal { position: absolute; left: 188px; top: 248px; width: 114px; height: 114px; }

  .product-cut {
    position: absolute; left: 0; width: 100%; text-align: center;
    top: 208px;
    font-family: "Arvo", serif; font-weight: 700; font-size: 92px;
    line-height: 1; color: var(--mid-blue);
  }
  .product-name {
    position: absolute; left: 0; width: 100%; text-align: center;
    top: 325px;
    font-family: "Montserrat", sans-serif; font-weight: 700; font-size: 136px;
    line-height: 1; letter-spacing: -2px; color: var(--navy);
  }
  .product-sub {
    position: absolute; left: 0; width: 100%; text-align: center;
    top: 437px; padding-left: 16px;
    font-family: "Noto Serif", serif; font-weight: 400; font-size: 58px;
    line-height: 1; letter-spacing: 17px; color: var(--bronze);
  }

  .story {
    position: absolute; left: 171px; width: 695px; top: 548px; height: 73px;
    border-top: 1.5px solid var(--rule);
    border-bottom: 1.5px solid var(--rule);
    text-align: center;
    font-family: "Merriweather", serif; font-weight: 300; font-size: 21.5px;
    line-height: 36px; color: var(--navy);
    padding-top: 0;
  }

  .care-strip {
    position: absolute; left: 0; top: 1062px; width: 369px; height: 66px;
    background: var(--white);
    border-radius: 0 33px 33px 0;
    display: flex; align-items: center; padding-left: 76px; gap: 10px;
  }
  .care-icons { width: 118px; height: 34px; }
  .care-label {
    font-family: "Oswald", sans-serif; font-weight: 300; font-size: 29px;
    color: var(--deep-wave); letter-spacing: 0.3px; margin-left: 6px;
  }

  .net-weight {
    position: absolute; right: 112px; top: 1045px; text-align: center;
    color: var(--white); font-family: "Oswald", sans-serif;
  }
  .net-weight .net-main { font-weight: 300; font-size: 37px; line-height: 40px; }
  .net-weight .net-sub { font-weight: 600; font-size: 22px; line-height: 26px; }
</style>
</head>
<body>
<main class="package">
  <svg class="waves" viewBox="0 0 1123 1300" preserveAspectRatio="none" aria-hidden="true">
    <path fill="var(--sky)" d="M0,910 C80,870 200,845 275,835 C280,760 420,722 560,722 C700,722 800,760 830,830 C835,880 815,935 860,920 C950,895 1050,865 1123,850 V1300 H0 Z"/>
    <ellipse class="window" cx="557" cy="850" rx="272" ry="106" fill="var(--white)"/>
    <path fill="var(--deep-wave)" d="M0,1020 C60,985 150,960 190,1000 C215,1025 160,1080 190,1100 C260,1120 350,1000 470,975 C560,960 650,990 630,1040 C615,1080 600,1110 660,1100 C800,1060 1000,990 1123,960 V1300 H0 Z"/>
  </svg>

  <svg class="brand-tab" viewBox="0 0 161 192" aria-hidden="true">
    <path d="M0,0 H161 V192 C120,175 60,172 0,180 Z" fill="var(--white)"/>
  </svg>
  <div class="brand-name">MARLO</div>

  <div class="tagline-top">TOP QUALITY</div>
  <div class="tagline-natural">All Natural</div>

  <svg class="seal" viewBox="0 0 114 114" aria-hidden="true">
    <circle cx="57" cy="57" r="55" fill="none" stroke="var(--rule)" stroke-width="2"/>
    <circle cx="57" cy="57" r="30" fill="none" stroke="var(--rule)" stroke-width="1.5"/>
  </svg>

  <div class="product-cut">cut</div>
  <h1 class="product-name">OCTOPUS</h1>
  <div class="product-sub">tako sashimi</div>

  <p class="story">The raw materials are caught in a very clean environment<br>processed in a modern factory with ZEK certification</p>

  <div class="care-strip">
    <svg class="care-icons" viewBox="0 0 118 34" aria-hidden="true">
      <circle cx="14" cy="17" r="13" fill="var(--deep-wave)"/>
      <path d="M8,17 a6,6 0 0 1 11,-3 M20,17 a6,6 0 0 1 -11,3" stroke="var(--white)" stroke-width="2.5" fill="none"/>
      <path d="M44,10 H62 M47,10 L49,30 H57 L59,10 M50,10 V6 H56 V10" stroke="var(--deep-wave)" stroke-width="2.2" fill="none"/>
      <path d="M88,4 H100 C100,14 97,17 94,17 C91,17 88,14 88,4 Z M94,17 V29 M89,30 H99" stroke="var(--deep-wave)" stroke-width="2.2" fill="none"/>
      <path d="M106,4 V30 M103,4 V12 C103,15 109,15 109,12 V4" stroke="var(--deep-wave)" stroke-width="2.2" fill="none"/>
    </svg>
    <span class="care-label">KEEP FROZEN</span>
  </div>

  <div class="net-weight">
    <div class="net-main">NET WT. 32 OZ</div>
    <div class="net-sub">(2.0 LB) 907g</div>
  </div>
</main>
</body>
</html>
```